Modern Business Card for Larkwell 2018

Our company assumes the best about people. We are creating an online community of entrepreneurs and business leaders who struggle with marketing their business online.

This business card should POP! We recently got a new logo and are launching a new website next month, so our business cards should make a statement that feels:
-Fresh
-Smart
-Trustworthy
-Fun

Target Market(s)

small business owners, entrepreneurs

Industry/Entity Type

Digital Marketing

Contact Information for Business Card

Dimensions: 3.5" x 2"

Font styles to use
Sans Serif

Colors
f37122
ffffff

Requirements
Must have
• We need a business card with a modern, bold design. We will use one side of the card as a lead-generation offer, so text on one side will need to fit up to 140 characters. The business card should stick to our core colors (orange, black, and white).
Nice to have
• We think a vertical "portrait" design could be interesting.
Should not have
• Should not look like a traditional business card. The round icon should stand out from a distance.

```html
<!DOCTYPE html>
<html lang="en">
<head>
<meta charset="utf-8">
<title>Larkwell Business Card</title>
<link rel="stylesheet" href="https://fonts.googleapis.com/css2?family=Roboto:wght@400;500;700&family=Norican&display=swap">
<style>
  :root {
    --orange: #f06a26;
    --orange-light: #f27a3e;
    --black: #000000;
    --white: #ffffff;
    --paper: #f2f2f2;
    --ink: #111111;
    --backdrop: #6e4c33;
  }
  html, body {
    margin: 0;
    padding: 0;
    width: 1200px;
    height: 960px;
    overflow: hidden;
    background: var(--backdrop);
    font-family: "Roboto", Arial, sans-serif;
  }
  .canvas { position: relative; width: 1200px; height: 960px; }
  .card {
    position: absolute;
    width: 342px;
    height: 600px;
    border-radius: 18px;
    overflow: hidden;
  }
  /* Front */
  .card-front { left: 262px; top: 163px; background: var(--paper); color: var(--ink); text-align: center; }
  .job-title { position: absolute; top: 63px; left: 0; right: 0; margin: 0; font-size: 15px; font-weight: 700; letter-spacing: 0.3px; }
  .person-name { position: absolute; top: 98px; left: 0; right: 0; margin: 0; font-family: "Norican", cursive; font-weight: 400; font-size: 48px; line-height: 1; }
  .email { position: absolute; top: 176px; left: 0; right: 0; margin: 0; font-size: 15.5px; font-weight: 700; }
  .front-mark { position: absolute; top: 410px; left: 0; right: 0; display: flex; flex-direction: column; align-items: center; gap: 14px; }
  .front-mark .dot { width: 70px; height: 70px; border-radius: 50%; background: var(--orange); }
  .front-mark .brand { font-size: 28px; font-weight: 700; color: var(--orange); letter-spacing: 1px; }
  /* Back */
  .card-back { left: 621px; top: 166px; background: var(--orange); color: var(--white); }
  .promise { position: absolute; top: 0; left: 0; right: 0; height: 225px; }
  .promise p { margin: 0; position: absolute; top: 70px; left: 0; right: 0; text-align: center; font-size: 18.5px; font-weight: 700; line-height: 25px; letter-spacing: 0.3px; }
  .offer { position: absolute; top: 225px; left: 0; right: 0; height: 148px; background: var(--black); }
  .offer-text { position: absolute; top: 26px; left: 81px; margin: 0; font-size: 15px; line-height: 19.5px; }
  .offer-link { position: absolute; top: 95px; left: 0; right: 0; margin: 0; text-align: center; font-size: 19.5px; font-weight: 700; }
  .signoff { position: absolute; top: 373px; left: 0; right: 0; bottom: 0; background: linear-gradient(135deg, var(--orange) 0%, var(--orange-light) 50%, var(--orange) 100%); text-align: center; }
  .signoff .dot { width: 40px; height: 40px; border-radius: 50%; background: var(--white); margin: 48px auto 0; }
  .signoff .brand { margin: 8px 0 0; font-size: 38px; font-weight: 700; letter-spacing: 1px; line-height: 44px; }
  .signoff .tagline { margin: 2px 0 0; font-size: 11.5px; font-weight: 700; letter-spacing: 0.8px; }
</style>
</head>
<body>
<main class="canvas">
  <section class="card card-front">
    <p class="job-title">STORY MARKETING COACH</p>
    <h1 class="person-name">Nolan Reyes</h1>
    <p class="email">nolan@larkwellnow.com</p>
    <div class="front-mark">
      <span class="dot"></span>
      <span class="brand">LARKWELL</span>
    </div>
  </section>

  <section class="card card-back">
    <div class="promise">
      <p>GROW YOUR AUDIENCE.<br>EARN WHAT YOU'RE WORTH.<br>LEAVE A BIGGER MARK.</p>
    </div>
    <div class="offer">
      <p class="offer-text">Get your free Larkwell<br>Starter Package and our<br>marketing guide today at</p>
      <p class="offer-link">Larkwellnow.com/start</p>
    </div>
    <div class="signoff">
      <div class="dot"></div>
      <p class="brand">LARKWELL</p>
      <p class="tagline">SHARE STORIES THAT SPARK CHANGE</p>
    </div>
  </section>
</main>
</body>
</html>
```